Visitenkarten-Design für Stillberaterin
Zielgruppe
Ich bin Stillberaterin ZMRPT, d. h. ich berate Mütter bei Stillschwierigkeiten. Meine Zielgruppe sind junge Familien, die sich vorab über das Stillen Ihres Kindes informieren möchten, Stillschwierigkeiten (z. B. Schmerzen, schlechte Gewichtszunahme usw.) haben oder Fragen rund ums Stillen haben (Medikamente, Stillen in besonderen Situationen...). Weiterhin biete ich Kurse für den Beikoststart oder zum Abstillen an.
Aufgabenstellung
Auf meiner Visitenkarte sollte mein Logo sowie alle Kontaktdaten klar und deutlich erkennbar sein. Die Farben sind dem Logo anzupassen. Die Schriftarten, die im Logo verwendet werden sind: Be Bright und Apple Tree

```html
<!DOCTYPE html>
<html lang="de">
<head>
<meta charset="utf-8">
<title>Visitenkarte Stillnest</title>
<link rel="stylesheet" href="https://fonts.googleapis.com/css2?family=Dancing+Script:wght@500&family=Indie+Flower&display=swap">
<style>
  :root {
    --page: #ffffff;
    --frame: #333333;
    --card: #7a877c;
    --pink: #e45aa6;
    --white: #ffffff;
    --text-font: "Indie Flower", cursive;
    --script-font: "Dancing Script", cursive;
  }
  * { margin: 0; padding: 0; box-sizing: border-box; }
  html, body { width: 1200px; height: 544px; overflow: hidden; background: var(--page); }
  .sheet {
    position: relative;
    width: 1200px; height: 544px;
    border: 1.5px solid var(--frame);
  }
  .card {
    position: absolute;
    top: 75px;
    width: 577px; height: 373px;
    background: var(--card);
  }
  .card--front { left: 16px; }
  .card--back { left: 598px; }

  /* Front */
  .brand-dot {
    position: absolute;
    left: 254px; top: 110px;
    width: 70px; height: 70px;
    border: 3px solid var(--pink);
    border-radius: 50%;
  }
  .brand-name {
    position: absolute;
    left: 0; right: 0; top: 222px;
    text-align: center;
    font-family: var(--text-font);
    font-size: 78px;
    line-height: 1;
    color: var(--pink);
  }
  .tagline {
    position: absolute;
    left: 0; right: 0; top: 310px;
    text-align: center;
    font-family: var(--text-font);
    font-size: 17px;
    color: var(--white);
  }

  /* Back */
  .person-name {
    position: absolute;
    left: 30px; top: 42px;
    font-family: var(--script-font);
    font-weight: 500;
    font-size: 48px;
    line-height: 1;
    color: var(--pink);
  }
  .info {
    position: absolute;
    left: 35px;
    font-family: var(--text-font);
    font-size: 18px;
    line-height: 24px;
    color: var(--white);
  }
  .info--role { left: 50px; top: 103px; font-size: 17px; }
  .info--address { top: 164px; }
  .info--contact { top: 232px; }
  .website-row {
    position: absolute;
    left: 44px; top: 298px;
    width: 500px; height: 36px;
    display: flex; align-items: center; gap: 10px;
  }
  .website-row .rule { flex: 1; height: 36px; }
  .website {
    font-family: var(--script-font);
    font-weight: 500;
    font-size: 30px;
    color: var(--pink);
    white-space: nowrap;
  }
</style>
</head>
<body>
  <div class="sheet">
    <section class="card card--front">
      <div class="brand-dot"></div>
      <div class="brand-name">Stillnest</div>
      <p class="tagline">Stillenberatung für Waldenbrück</p>
    </section>

    <section class="card card--back">
      <h1 class="person-name">Mirela Hansen</h1>
      <p class="info info--role">Fachkrankenschwester<br>Still- &amp;Laktationsberaterin ZMRPT</p>
      <p class="info info--address">Am Lindenhang 4<br>97531 Musterbach</p>
      <p class="info info--contact">Telefon: 01234 5827160<br>E-Mail: mirela@stillnest-beratung.de</p>
      <div class="website-row">
        <svg class="rule" viewBox="0 0 90 36" preserveAspectRatio="none" aria-hidden="true">
          <line x1="2" y1="18" x2="88" y2="18" stroke="#e45aa6" stroke-width="2"/>
        </svg>
        <span class="website">www.stillnest-beratung.de</span>
        <svg class="rule" viewBox="0 0 90 36" preserveAspectRatio="none" aria-hidden="true">
          <line x1="2" y1="18" x2="88" y2="18" stroke="#e45aa6" stroke-width="2"/>
        </svg>
      </div>
    </section>
  </div>
</body>
</html>
```